business card with 2 locations on 1 card

I need a modern looking business card that I would use at 2 different locations. Possibly 1 location on 1 side and other location on other side. One should be able to distinguish the 2 locations immediately before having to read the address or description on card. You can take a look at my website to see what I'm drawn to. The logo is brand new that I just purchased on Craft Hive. I want to emphasize family.
Updates

Let's not use the yellow and blue colors. Added Thursday, August 31, 2017

Target Market(s)

women and children

Industry/Entity Type

Health And Wellness

Contact Information for Business Card

Business name: Willow Brook Chiropractic & Acupuncture
My name: Lorin Daske
Job title: DC, MSOM, LAc (NM), CCN

Location 1
Address: 4817 Marlowe Blvd, Suite C-210, Ashford, TX 75301
Phone: (469) 555-0182
Fax: (972) 555-0137

Location 2
Address: 1936 Belvane Road, Suite 340, Kellerby, TX 75388
Phone: (469) 555-0169
Fax: (972) 555-0137

Email: drlorindaske@mailnest.example
Website: www.drlorindaske.example

Font styles to use
Serif
Sans Serif

Colors

Designer to choose colors to be used in the design.

Requirements
Must have
• distinction between 2 locations.
Nice to have
• Colors preference below is there. But I like to see what you come up with too!

```html
<!DOCTYPE html>
<html lang="en">
<head>
<meta charset="utf-8">
<title>Willow Brook Chiropractic &amp; Acupuncture — Business Card</title>
<link rel="stylesheet" href="https://fonts.googleapis.com/css2?family=Cinzel:wght@600&family=Lato:wght@400&display=swap">
<style>
  :root {
    --page-bg: #d9dde1;
    --card-top: #f4f5f6;
    --card-bottom: #e6e9eb;
    --brand-green: #1f4a46;
    --text-grey: #3e4347;
    --label-green: #2f4a47;
    --band-text: #e4ecea;
  }
  * { margin: 0; padding: 0; box-sizing: border-box; }
  html, body { width: 1200px; height: 970px; overflow: hidden; }
  body { background: var(--page-bg); position: relative; font-family: "Lato", Arial, sans-serif; }

  .card {
    position: absolute; left: 80px; top: 188px;
    width: 1040px; height: 593px;
    border-radius: 22px; overflow: hidden;
    background: linear-gradient(180deg, var(--card-top), var(--card-bottom));
    box-shadow: 0 12px 30px rgba(0,0,0,0.18);
  }

  .brand-mark {
    position: absolute; left: 119px; top: 41px;
    width: 186px; height: 186px; border-radius: 50%;
    border: 7px solid var(--brand-green);
  }
  .brand-name, .brand-sub {
    position: absolute; left: 32px; width: 360px; text-align: center;
    white-space: nowrap; color: var(--brand-green);
    font-family: "Cinzel", Georgia, serif; font-weight: 600;
  }
  .brand-name { top: 240px; font-size: 41px; line-height: 48px; }
  .brand-sub { top: 289px; font-size: 16px; line-height: 20px; letter-spacing: 0.3px; }

  .person { position: absolute; right: 44px; top: 50px; text-align: right; white-space: nowrap; }
  .person-name { font-family: "Cinzel", Georgia, serif; font-weight: 600; font-size: 37px; line-height: 44px; color: var(--brand-green); }
  .person-title { font-size: 25px; line-height: 30px; color: var(--text-grey); }

  .office { position: absolute; top: 350px; color: var(--text-grey); font-size: 25px; line-height: 33px; white-space: nowrap; }
  .office--ashford { left: 49px; }
  .office--kellerby { left: 487px; }
  .office-label { font-size: 22px; line-height: 30px; color: var(--label-green); }
  .contact-line { display: flex; align-items: center; gap: 6px; height: 33px; }
  .contact-line svg { width: 30px; height: 30px; flex: none; }

  .footer-band {
    position: absolute; left: 0; bottom: 0; width: 100%; height: 60px;
    background: var(--brand-green); color: var(--band-text);
    font-size: 26px; line-height: 60px; white-space: nowrap;
  }
  .footer-email { position: absolute; left: 49px; top: 0; display: flex; align-items: center; gap: 10px; height: 60px; }
  .footer-email svg { width: 30px; height: 30px; }
  .footer-web { position: absolute; left: 493px; top: 0; }
</style>
</head>
<body>
  <main class="card">
    <span class="brand-mark"></span>
    <div class="brand-name">Willow Brook</div>
    <div class="brand-sub">Chiropractic &amp; Acupuncture</div>

    <div class="person">
      <div class="person-name">Lorin Daske</div>
      <div class="person-title">DC, MSOM, LAc (NM), CCN</div>
    </div>

    <section class="office office--ashford">
      <div class="office-label">Ashford's Office</div>
      <div>4817 Marlowe Blvd,</div>
      <div>Suite C-210, Ashford, TX 75301</div>
      <div class="contact-line">
        <svg viewBox="0 0 30 30" aria-hidden="true"><circle cx="15" cy="15" r="13" fill="none" stroke="#3e4347" stroke-width="2.2"/><path d="M8 13c0-3 14-3 14 0v1.5h-3.5v-1.5h-7v1.5H8z M10 15h10l1.5 6h-13z" fill="#3e4347"/><circle cx="15" cy="18" r="1.8" fill="#e9ecee"/></svg>
        <span>(469) 555-0182</span>
      </div>
      <div class="contact-line">
        <svg viewBox="0 0 30 30" aria-hidden="true"><circle cx="15" cy="15" r="13" fill="none" stroke="#3e4347" stroke-width="2.2"/><rect x="10" y="7.5" width="10" height="6" fill="#3e4347"/><rect x="7.5" y="12.5" width="15" height="8" rx="1.5" fill="#3e4347"/><rect x="10" y="18" width="10" height="5" fill="#3e4347" stroke="#e9ecee" stroke-width="1"/></svg>
        <span>(972) 555-0137</span>
      </div>
    </section>

    <section class="office office--kellerby">
      <div class="office-label">Kellerby's Office</div>
      <div>1936 Belvane Road,</div>
      <div>Suite 340, Kellerby, TX 75388</div>
      <div class="contact-line">
        <svg viewBox="0 0 30 30" aria-hidden="true"><circle cx="15" cy="15" r="13" fill="none" stroke="#3e4347" stroke-width="2.2"/><path d="M8 13c0-3 14-3 14 0v1.5h-3.5v-1.5h-7v1.5H8z M10 15h10l1.5 6h-13z" fill="#3e4347"/><circle cx="15" cy="18" r="1.8" fill="#e9ecee"/></svg>
        <span>(469) 555-0169</span>
      </div>
      <div class="contact-line">
        <svg viewBox="0 0 30 30" aria-hidden="true"><circle cx="15" cy="15" r="13" fill="none" stroke="#3e4347" stroke-width="2.2"/><rect x="10" y="7.5" width="10" height="6" fill="#3e4347"/><rect x="7.5" y="12.5" width="15" height="8" rx="1.5" fill="#3e4347"/><rect x="10" y="18" width="10" height="5" fill="#3e4347" stroke="#e9ecee" stroke-width="1"/></svg>
        <span>(972) 555-0137</span>
      </div>
    </section>

    <footer class="footer-band">
      <div class="footer-email">
        <svg viewBox="0 0 30 30" aria-hidden="true"><circle cx="15" cy="15" r="13" fill="none" stroke="#e4ecea" stroke-width="2"/><rect x="8" y="10" width="14" height="10" fill="none" stroke="#e4ecea" stroke-width="1.8"/><path d="M8 10l7 6 7-6" fill="none" stroke="#e4ecea" stroke-width="1.8"/></svg>
        <span>drlorindaske@mailnest.example</span>
      </div>
      <div class="footer-web">www.drlorindaske.example</div>
    </footer>
  </main>
</body>
</html>
```